Chiropractic Business Card

I need a business card designed to help me stand apart from my competition. I really like simple, clean designs that appear open and inviting. I would like the designs to incorporate the color blue, green, or both. I really like the attached picture because it highlights that I just don't treat "back pain" and it being a nice computer graphic helps show that I have a modern practice. "Modern practice" meaning merging technology and most current research in my patient care.

My information is:

Wesley Harmon, DC
Phone- (707) 555-0182
Email- drwesleyharmon@mailbox-example.com
Website- www.fernleachiropractic-example.com
Address- 248 Pellham Street, Sonoma, CA 95400

Jpeg and pdf attached of Fernlea Chiropractic logo.
Updates

Atmosphere to be clean lines and solid colors to be have gradient fading, but don't want too much going on with the fading. Simple.

Target Market(s)

Active adults who are health conscious between the ages of 20-70

Industry/Entity Type

Computer

Colors
0455a3
85cae6

Requirements
Must have
• Change color of Fernlea chiropractic logo (maroon) to fit the rest of the design.
Nice to have
• Can separate the running image from the black background to have it work with the design.

```html
<!DOCTYPE html>
<html lang="en">
<head>
<meta charset="utf-8">
<title>Fernlea Chiropractic – Business Card</title>
<link href="https://fonts.googleapis.com/css2?family=Cinzel:wght@400;700&family=Open+Sans:wght@400&display=swap" rel="stylesheet">
<style>
  :root {
    --blue-deep: #0455a3;
    --blue-mid: #1f7fc9;
    --blue-light: #85cae6;
    --paper: #ffffff;
    --ink: #2b2b2b;
    --backdrop: #e9ecef;
  }
  * { box-sizing: border-box; margin: 0; padding: 0; }
  html, body { width: 1200px; height: 800px; overflow: hidden; }
  body {
    background: var(--backdrop);
    display: flex; align-items: center; justify-content: center; gap: 60px;
    font-family: "Open Sans", Arial, sans-serif;
  }

  /* ---------- Front ---------- */
  .card-front {
    position: relative; width: 700px; height: 400px;
    background: var(--paper); overflow: hidden;
    box-shadow: 0 6px 24px rgba(0,0,0,.18);
  }
  .brand { position: absolute; left: 34px; top: 26px; width: 360px; color: var(--blue-mid); }
  .brand-name {
    font-family: "Cinzel", Georgia, serif; font-weight: 700;
    font-size: 30px; line-height: 1.05; letter-spacing: 1px; text-transform: uppercase;
  }
  .brand-rule { height: 2px; background: var(--blue-mid); margin: 6px 0 4px; }
  .brand-tag {
    font-family: "Cinzel", Georgia, serif; font-weight: 700;
    font-size: 9.5px; letter-spacing: .5px; text-transform: uppercase; line-height: 1.45;
  }
  .name-panel {
    position: absolute; left: 400px; top: 112px; width: 300px; height: 150px;
    background: linear-gradient(135deg, var(--blue-mid), var(--blue-deep));
  }
  .holder-name {
    position: absolute; right: 26px; top: 22px;
    font-family: "Cinzel", Georgia, serif; font-size: 24px; color: var(--paper);
  }
  .contact-list { position: absolute; left: 34px; top: 160px; list-style: none; }
  .contact-list li {
    display: flex; align-items: center; gap: 12px;
    font-size: 14.5px; color: var(--ink); height: 27px;
  }
  .contact-icon {
    width: 17px; height: 17px; background: var(--blue-mid); border-radius: 2px;
    display: flex; align-items: center; justify-content: center; flex: none;
  }
  .contact-icon svg { width: 11px; height: 11px; fill: var(--paper); }
  .base-line { position: absolute; left: 0; right: 0; top: 334px; height: 3px; background: var(--blue-mid); }
  .base-band {
    position: absolute; left: 0; right: 0; top: 345px; bottom: 0;
    background: linear-gradient(90deg, var(--blue-light), var(--blue-mid) 50%, var(--blue-deep));
  }
  .figure-front {
    position: absolute; left: 450px; top: 190px; width: 240px; height: 205px;
    border-radius: 50% 45% 10px 10px;
    background: radial-gradient(ellipse at 50% 45%, rgba(200,220,235,.9), rgba(110,150,185,.75) 60%, rgba(70,110,150,.25));
  }

  /* ---------- Back ---------- */
  .card-back {
    position: relative; width: 229px; height: 400px; overflow: hidden;
    background: linear-gradient(180deg, var(--blue-mid), var(--blue-light) 55%, var(--blue-mid));
    box-shadow: 0 6px 24px rgba(0,0,0,.18);
  }
  .back-stripe { position: absolute; top: 0; bottom: 0; width: 3px; background: var(--paper); }
  .back-stripe.left { left: 26px; }
  .back-stripe.right { left: 170px; }
  .back-brand {
    position: absolute; left: 40px; top: 14px; height: 210px;
    writing-mode: vertical-rl; color: var(--paper);
    display: flex; gap: 4px;
  }
  .back-brand .brand-name { font-size: 26px; }
  .back-brand .brand-tag { font-size: 8px; }
  .back-brand .brand-rule { width: 2px; height: auto; margin: 0 3px; background: var(--paper); }
  .figure-back {
    position: absolute; left: 10px; top: 220px; width: 210px; height: 170px;
    border-radius: 40% 50% 8px 8px;
    background: radial-gradient(ellipse at 50% 50%, rgba(215,230,242,.75), rgba(130,170,205,.5) 60%, rgba(90,140,190,0));
  }
</style>
</head>
<body>

<section class="card-front">
  <div class="brand">
    <p class="brand-name">Fernlea Chiropractic Offices Inc.</p>
    <div class="brand-rule"></div>
    <p class="brand-tag">Fernlea Chiropractic Neurology Group<br>Board Certified Chiropractic Neurologists</p>
  </div>

  <div class="name-panel">
    <p class="holder-name">Wesley Harmon, DC</p>
  </div>

  <ul class="contact-list">
    <li><span class="contact-icon"><svg viewBox="0 0 24 24"><path d="M6.6 10.8a15 15 0 0 0 6.6 6.6l2.2-2.2a1 1 0 0 1 1-.25 11.4 11.4 0 0 0 3.6.57 1 1 0 0 1 1 1V20a1 1 0 0 1-1 1A17 17 0 0 1 3 4a1 1 0 0 1 1-1h3.5a1 1 0 0 1 1 1c0 1.25.2 2.45.57 3.6a1 1 0 0 1-.25 1z"/></svg></span>(707) 555-0182</li>
    <li><span class="contact-icon"><svg viewBox="0 0 24 24"><path d="M2 5h20v14H2zM4 7v.5l8 5 8-5V7l-8 5z"/></svg></span>drwesleyharmon@mailbox-example.com</li>
    <li><span class="contact-icon"><svg viewBox="0 0 24 24"><path d="M12 2a10 10 0 1 0 0 20 10 10 0 0 0 0-20zm0 2c1 0 2.3 2 2.8 5H9.2C9.7 6 11 4 12 4zM4.3 11h4.7a19 19 0 0 0 0 2H4.3a8 8 0 0 1 0-2zm6.7 0h2a17 17 0 0 1 0 2h-2a17 17 0 0 1 0-2zm4 0h4.7a8 8 0 0 1 0 2H15a19 19 0 0 0 0-2zM9.2 15h5.6c-.5 3-1.8 5-2.8 5s-2.3-2-2.8-5z"/></svg></span>www.fernleachiropractic-example.com</li>
    <li><span class="contact-icon"><svg viewBox="0 0 24 24"><path d="M12 2a7 7 0 0 0-7 7c0 5 7 13 7 13s7-8 7-13a7 7 0 0 0-7-7zm0 9.5A2.5 2.5 0 1 1 12 6.5a2.5 2.5 0 0 1 0 5z"/></svg></span>248 Pellham Street, Sonoma, CA 95400</li>
  </ul>

  <div class="base-line"></div>
  <div class="base-band"></div>
  <div class="figure-front" role="img" aria-label="Translucent computer-rendered runner with visible skeleton and red highlighted joints"></div>
</section>

<section class="card-back">
  <div class="back-stripe left"></div>
  <div class="back-stripe right"></div>
  <div class="back-brand">
    <p class="brand-name">Fernlea Chiropractic Offices Inc.</p>
    <div class="brand-rule"></div>
    <p class="brand-tag">Fernlea Chiropractic Neurology Group<br>Board Certified Chiropractic Neurologists</p>
  </div>
  <div class="figure-back" role="img" aria-label="Faded computer-rendered runner skeleton with red highlighted joints"></div>
</section>

</body>
</html>
```